Yacht, Boats, Watersports company needs a redesign of business card

Hello Designers!
We are a Boat dealership company that sells fun in the water, we sell boats, Yachts, Kayaks and also yacht WaterSport toys. We are looking to redesign our business cards in to something a little bit more sophisticated. in a way that we can make better use of our company colors. I'm attaching a zipped file containing the company 3 sets of company logo which one is an horizontal another one is a vertical and also a chromed 3d logo. Also is included two set of business cards that we use and also some designs that i think it's interesting. We use PMS 2026c Orange and PMS 7687C Blue. I would like to see at least two different options with the orange as accent and also using blue as an accent color. It's really important for the business cards to have a font option and size that is legible to most people. Our current website is wwww.corvellamarine.com. Please visit if you want to have a better feeling of the Boat dealership
You can send Single sided or double side options. We are now using single sided but we may be open for a double side option if we really like the design.
Target Market(s)
Marine, boat sales, yacht sales, water toys sales/
Contact Information for Business Card
Name: Dale Pritchett
Address: 718 West Halden Lane,
Dania Beach, FL 33019
Phone: 954-382-7146
Fax: 954:382-7139
Cell: 954-451-8320
Email: 212@corvellamarine.com
Website: corvellamarine.com
Requirements
Must have
- the current information of the business card provided.
logo
use the PMS Colors
Nice to have
- a touch of elegance and sophistication but simple
Should not have
- should not have any typography that is hard to read, the card should be simple but yet sophisticated.

```html
<!DOCTYPE html>
<html lang="en">
<head>
<meta charset="utf-8">
<title>Corvella Marine — Business Card</title>
<link rel="stylesheet" href="https://fonts.googleapis.com/css2?family=Arimo:wght@400;700&display=swap">
<style>
  :root {
    --brand-orange: #e2401c;
    --brand-blue: #1d3a7a;
    --paper-white: #f7f7f5;
    --ink-grey: #5d5d62;
    --backdrop: #e4e4e6;
  }
  html, body {
    margin: 0;
    width: 1200px;
    height: 1000px;
    overflow: hidden;
    background: var(--backdrop);
    font-family: "Arimo", Arial, sans-serif;
  }
  .card-set {
    position: relative;
    width: 1200px;
    height: 1000px;
  }
  .card {
    position: absolute;
    top: 200px;
    width: 340px;
    height: 595px;
    box-shadow: 0 10px 30px rgba(0,0,0,0.12);
  }
  /* Back side */
  .card--back {
    left: 220px;
    background: var(--brand-orange);
  }
  .card--back .frame {
    position: absolute;
    inset: 18px;
    border: 1px solid rgba(255,255,255,0.9);
  }
  .back-mark {
    position: absolute;
    top: 268px;
    left: 0;
    right: 0;
    display: flex;
    align-items: center;
    justify-content: center;
    gap: 8px;
    color: #fff;
    font-weight: 700;
    font-size: 13px;
    letter-spacing: 0.08em;
    text-transform: uppercase;
  }
  .back-mark .dot {
    width: 22px;
    height: 22px;
    border: 2px solid #fff;
    border-radius: 50%;
    box-sizing: border-box;
  }
  .back-wordmark {
    position: absolute;
    bottom: 40px;
    left: 0;
    right: 0;
    text-align: center;
    color: #fff;
    font-weight: 700;
    font-size: 22px;
    letter-spacing: 0.06em;
    text-transform: uppercase;
  }
  /* Front side */
  .card--front {
    left: 640px;
    background: var(--paper-white);
  }
  .front-logo {
    position: absolute;
    top: 120px;
    left: 0;
    right: 0;
    display: flex;
    flex-direction: column;
    align-items: center;
    gap: 14px;
  }
  .front-logo .dot {
    width: 46px;
    height: 46px;
    border: 4px solid var(--brand-blue);
    border-radius: 50%;
    box-sizing: border-box;
  }
  .front-logo .name {
    color: var(--brand-blue);
    font-weight: 700;
    font-size: 24px;
    letter-spacing: 0.06em;
    text-transform: uppercase;
  }
  .contact {
    position: absolute;
    top: 360px;
    left: 44px;
    right: 20px;
    color: var(--ink-grey);
    font-size: 15px;
    line-height: 1.35;
  }
  .contact .person {
    margin: 0 0 14px 6px;
    font-size: 15px;
  }
  .contact dl {
    display: grid;
    grid-template-columns: 50px auto;
    column-gap: 16px;
    margin: 0 0 14px;
  }
  .contact dt {
    color: var(--brand-orange);
    text-align: right;
  }
  .contact dd { margin: 0; }
  .contact address {
    font-style: normal;
  }
</style>
</head>
<body>
  <main class="card-set">
    <section class="card card--back" aria-label="Card back">
      <div class="frame"></div>
      <div class="back-mark"><span class="dot"></span><span>Corvella Marine</span></div>
      <div class="back-wordmark">Corvella Marine</div>
    </section>

    <section class="card card--front" aria-label="Card front">
      <div class="front-logo">
        <span class="dot"></span>
        <span class="name">Corvella Marine</span>
      </div>
      <div class="contact">
        <p class="person">Dale Pritchett</p>
        <dl>
          <dt>Tel.:</dt><dd>954-382-7146</dd>
          <dt>Fax:</dt><dd>954:382-7139</dd>
          <dt>Cell:</dt><dd>954-451-8320</dd>
          <dt>Web:</dt><dd>corvellamarine.com</dd>
          <dt>Email:</dt><dd>212@corvellamarine.com</dd>
        </dl>
        <address>718 West Halden Lane,<br>Dania Beach, FL 33019</address>
      </div>
    </section>
  </main>
</body>
</html>
```